Web app with questionnaires and graphs

For crewlifters.nl I want a clean design with good UX . It's a web app that let's users fill in questionnaires to assess things like team culture, psychological safety and so on. Colorwise should work with the Velmor Institute green logo. The app displays graphs (bar, line, pie) so these should also be incorporated.

```html
<!DOCTYPE html>
<html lang="en">
<head>
<meta charset="utf-8">
<title>Crew Lifters – Team tools</title>
<link href="https://fonts.googleapis.com/css2?family=Fira+Sans:wght@400;500;600;700&display=swap" rel="stylesheet">
<style>
:root{
  --green:#33b34a;
  --green-soft:#dff1e2;
  --purple:#7d5ca8;
  --ink:#222222;
  --muted:#444444;
  --footer:#313131;
  --stage:#262626;
  --line:#e4e4e4;
  --tile:#f1f1f1;
  --tab-dark:#454545;
}
*{box-sizing:border-box;margin:0;padding:0}
html,body{width:1200px;height:5277px;overflow:hidden;background:#ffffff;font-family:"Fira Sans",Arial,sans-serif;color:var(--ink)}
.stage{position:absolute;left:35px;width:1130px;height:1697px;background:var(--stage)}
.stage--tools{top:62px}
.stage--form{top:1794px}
.stage--results{top:3522px}
.screen{position:absolute;left:37px;top:72px;width:1058px;height:1556px;background:#fff;border-radius:10px;overflow:hidden}
.abs{position:absolute}

/* header */
.app-header{position:absolute;left:0;top:27px;width:100%;height:57px}
.brand{position:absolute;left:27px;top:8px;color:var(--ink);font-weight:600;line-height:1.1}
.brand__name{font-size:17px;letter-spacing:.3px}
.brand__by{font-size:10px;padding-left:58px}
.app-header__bar{position:absolute;left:195px;right:6px;top:0;height:57px;background:var(--green);clip-path:polygon(26px 0,100% 0,100% 100%,0 100%)}
.nav{position:absolute;top:0;height:57px;line-height:57px;color:#fff;font-size:14px;font-weight:600;letter-spacing:.5px}
.nav--tools{left:584px}.nav--about{left:717px}
.feedback{position:absolute;left:896px;top:6px;width:149px;height:45px;background:#fff;border-radius:8px;color:var(--green);font-weight:600;font-size:14px;display:flex;align-items:center;justify-content:center;gap:8px;letter-spacing:.4px}

/* type */
.page-title{left:0;width:100%;text-align:center;font-size:34px;font-weight:700;letter-spacing:.5px}
.lead{left:20px;right:20px;text-align:center;font-size:14px;line-height:25px;color:var(--muted)}
.section-title{font-size:26px;font-weight:400}
.body-text{font-size:13px;line-height:25px;color:var(--muted)}

/* tool cards */
.tool-card{position:absolute;left:107px;width:845px;height:219px;border:2px solid var(--line);border-radius:8px;box-shadow:0 2px 6px rgba(0,0,0,.06)}
.tool-card__art{position:absolute;top:10px;width:221px;height:195px;border-radius:6px;background:radial-gradient(ellipse at 50% 55%,#bfe3c5 0,#e2f1e4 45%,var(--tile) 72%)}
.tool-card__art--left{left:10px}.tool-card__art--right{right:10px}
.tool-card__body{position:absolute;top:30px}
.tool-card__body--right{left:266px;width:540px}
.tool-card__body--left{left:18px;width:540px}
.tool-card h3{font-size:24px;font-weight:500;letter-spacing:.3px;margin-bottom:14px}
.tool-card p{font-size:14px;line-height:21px;color:var(--ink);width:420px;margin-bottom:18px}
.btn{display:inline-block;background:var(--purple);color:#fff;font-size:13px;font-weight:500;letter-spacing:.5px;border-radius:7px;height:49px;line-height:49px;padding:0 16px}

/* footer */
.footer{position:absolute;left:0;top:1310px;width:100%;height:246px;background:var(--footer);color:#fff;font-size:13px}
.footer__meta{position:absolute;left:37px;top:70px;line-height:25px}
.footer__col{position:absolute;top:54px;line-height:25px}
.footer__col h4{font-size:18px;font-weight:500;margin-bottom:8px}
.footer__col--about{left:496px}.footer__col--tools{left:800px}

/* form */
.link-card{position:absolute;left:105px;top:426px;width:851px;height:384px;border:2px solid var(--line);border-radius:8px;box-shadow:0 2px 6px rgba(0,0,0,.06)}
.link-card__art{position:absolute;left:14px;top:14px;width:359px;height:351px;border-radius:6px;background:radial-gradient(ellipse at 50% 50%,#b9e1c0 0,#dcefdf 48%,var(--tile) 75%)}
.field-label{position:absolute;left:400px;font-size:13px;font-weight:600}
.field{position:absolute;left:400px;width:422px;height:47px;border:2px solid #bdbdbd;border-radius:9px;font-size:12px;line-height:43px;padding-left:10px}
.field-note{position:absolute;left:400px;font-size:11px}
.btn--small{position:absolute;left:400px;top:305px;height:48px;line-height:48px;width:141px;text-align:center;padding:0;font-size:13px}
.accordion{position:absolute;left:37px;width:982px;height:53px;background:var(--green);border-radius:6px;color:#fff;font-size:15px;font-weight:500;line-height:53px;padding-left:18px}
.accordion svg{position:absolute;right:18px;top:19px}

/* results */
.tab{position:absolute;top:141px;height:53px;line-height:55px;text-align:center;color:#fff;font-size:23px;border-radius:5px 5px 0 0}
.tab--active{left:59px;width:256px;background:var(--green)}
.tab--idle{left:330px;width:184px;background:var(--tab-dark)}
.tab-rule{position:absolute;left:49px;top:194px;width:962px;height:3px;background:var(--tab-dark)}
.toggle-label{position:absolute;left:834px;top:152px;font-size:15px;font-weight:500}
.toggle{position:absolute;left:937px;top:150px;width:70px;height:34px;border-radius:17px;background:#d9d9d9}
.toggle::after{content:"";position:absolute;left:2px;top:2px;width:30px;height:30px;border-radius:50%;background:var(--green)}
.chart-card{position:absolute;left:105px;width:849px;border:2px solid var(--line);border-radius:8px;box-shadow:0 2px 6px rgba(0,0,0,.06)}
.chart-card p{position:absolute;left:26px;top:40px;width:800px;font-size:13px;line-height:25px;color:var(--muted)}
.chart-card svg{position:absolute;left:0;top:0}
.chart-card text{font-family:"Fira Sans",Arial,sans-serif;font-size:14px;fill:var(--ink)}
</style>
</head>
<body>

<!-- Screen 1: tools overview -->
<section class="stage stage--tools">
  <div class="screen">
    <header class="app-header">
      <div class="brand"><div class="brand__name">CREW LIFTERS</div><div class="brand__by">by Velmor Institute</div></div>
      <div class="app-header__bar"></div>
      <a class="nav nav--tools">TOOLS</a><a class="nav nav--about">ABOUT US</a>
      <div class="feedback"><svg width="22" height="22" viewBox="0 0 22 22"><circle cx="11" cy="11" r="9.5" fill="none" stroke="#33b34a" stroke-width="1.6"/><rect x="10" y="9" width="2" height="7" fill="#33b34a"/><circle cx="11" cy="6.5" r="1.2" fill="#33b34a"/></svg>FEEDBACK</div>
    </header>

    <h1 class="abs page-title" style="top:130px">FREE TOOLS TO STRENGTHEN YOUR TEAMS</h1>
    <p class="abs lead" style="top:190px">To make your team - and organization - better, you first need to map out how things are now. Our tools give you insight into the health of your team and<br>the culture of the organization. With the results in hand, you can start improving your team and organization. Each tool gives you useful tips and tricks<br>to make improvements. Are you stuck? We are happy to help you!</p>

    <article class="tool-card" style="top:328px">
      <div class="tool-card__art tool-card__art--left" role="img" aria-label="Illustration of team members building blocks together"></div>
      <div class="tool-card__body tool-card__body--right">
        <h3>PSYCHOLOGICAL SAFETY</h3>
        <p>Measure the psychological safety in your team completely anonymously.</p>
        <span class="btn">GO TO THE QUESTIONNAIRE</span>
      </div>
    </article>

    <article class="tool-card" style="top:582px">
      <div class="tool-card__body tool-card__body--left">
        <h3>HARLOW CULTURE SCAN</h3>
        <p>With this tool you visualize the general culture of your organization. Is it mainly a Control, Competence, Collaboration or Cultivation culture?</p>
        <span class="btn">GO TO THE QUESTIONNAIRE</span>
      </div>
      <div class="tool-card__art tool-card__art--right" role="img" aria-label="Illustration of colleagues shaking hands"></div>
    </article>

    <article class="tool-card" style="top:836px">
      <div class="tool-card__art tool-card__art--left" role="img" aria-label="Illustration of a developer at a desk with code screens"></div>
      <div class="tool-card__body tool-card__body--right">
        <h3>DEVELOPER CULTURE TEST</h3>
        <p>Measure the Development culture in your organization. Do you have what it takes to attract and retain talent?</p>
        <span class="btn">GO TO THE QUESTIONNAIRE</span>
      </div>
    </article>

    <h2 class="abs page-title" style="top:1130px">INTERVENTIONS</h2>
    <p class="abs lead" style="top:1188px">Using these tools is a first step towards improvement. The tools give you insight with which you can apply suitable interventions. For example, working on<br>the psychological safety of a team by getting to know each other better (do an escape room together, or create one yourself ) and rewarding interpersonal<br>risks (holding a failure party).</p>

    <footer class="footer">
      <div class="footer__meta">© 2020 Quillbyte for Velmor Institute<br>Tools that help your teams further.<br><br>Need more help? We are happy to help you.</div>
      <div class="footer__col footer__col--about"><h4>About Us</h4>Privacy &amp; security</div>
      <div class="footer__col footer__col--tools"><h4>Tools</h4>Psychological safety<br>Harlow culture scan<br>Developer culture scan</div>
    </footer>
  </div>
</section>

<!-- Screen 2: psychological safety -->
<section class="stage stage--form">
  <div class="screen">
    <header class="app-header">
      <div class="brand"><div class="brand__name">CREW LIFTERS</div><div class="brand__by">by Velmor Institute</div></div>
      <div class="app-header__bar"></div>
      <a class="nav nav--tools">TOOLS</a><a class="nav nav--about">ABOUT US</a>
      <div class="feedback"><svg width="22" height="22" viewBox="0 0 22 22"><circle cx="11" cy="11" r="9.5" fill="none" stroke="#33b34a" stroke-width="1.6"/><rect x="10" y="9" width="2" height="7" fill="#33b34a"/><circle cx="11" cy="6.5" r="1.2" fill="#33b34a"/></svg>FEEDBACK</div>
    </header>

    <h1 class="abs page-title" style="top:128px">PSYCHOLOGICAL SAFETY</h1>
    <p class="abs lead" style="top:188px">To make your team - and organization - better, you first need to map out how things are now. Our tools give you insight into the health of your team and<br>the culture of the organization. With the results in hand, you can start improving your team and organization. Each tool gives you useful tips and tricks<br>to make improvements. Are you stuck? We are happy to help you!</p>

    <h2 class="abs section-title" style="top:290px;left:0;width:100%;text-align:center">Give the Link To the Questionnaire</h2>
    <p class="abs body-text" style="top:343px;left:37px;width:984px;text-align:center">Our tools give you insight into the health of your team and the culture of the organization. With the results in hand, you can start improving your team and orga-<br>nization. Each tool gives you useful tips and tricks to make improvements. Are you stuck? We are happy to help you!</p>

    <div class="link-card">
      <div class="link-card__art" role="img" aria-label="Illustration of a person presenting a dashboard with charts"></div>
      <label class="field-label" style="top:58px">TEAM NAME</label>
      <div class="field" style="top:96px">Team Awesome</div>
      <label class="field-label" style="top:172px">E-MAIL</label>
      <div class="field" style="top:207px">janine@example.org</div>
      <div class="field-note" style="top:270px">We will never distribute your email address</div>
      <span class="btn btn--small">GENERATE LINK</span>
    </div>

    <h3 class="abs section-title" style="top:864px;left:37px;font-weight:500">Wat is psychologische veiligheid?</h3>
    <p class="abs body-text" style="top:917px;left:37px;width:984px">Our tools give you insight into the health of your team and the culture of the organization. With the results in hand, you can start improving your team and organiza<br>tion. Each tool gives you useful tips and tricks to make improvements. Are you stuck? We are happy to help you! Our tools give you insight into the health of your team<br>and the culture of the organization. With the results in hand, you can start improving your team and your organiza tion. Each tool gives you useful tips and tricks to make<br>improvements. Are you stuck? We are happy to help you!</p>

    <div class="accordion" style="top:1043px">Wat is psychologische veiligheid?<svg width="18" height="12" viewBox="0 0 18 12"><path d="M2 10 9 3l7 7" fill="none" stroke="#fff" stroke-width="2"/></svg></div>
    <p class="abs body-text" style="top:1110px;left:37px;width:984px">Our tools give you insight into the health of your team and the culture of the organization. With the results in hand, you can start improving your team and organiza<br>tion. Each tool gives you useful tips and tricks to make improvements.</p>
    <div class="accordion" style="top:1177px">Wat is psychologische veiligheid?<svg width="18" height="12" viewBox="0 0 18 12"><path d="M2 2l7 7 7-7" fill="none" stroke="#fff" stroke-width="2"/></svg></div>

    <footer class="footer">
      <div class="footer__meta">© 2020 Quillbyte for Velmor Institute<br>Tools that help your teams further.<br><br>Need more help? We are happy to help you.</div>
      <div class="footer__col footer__col--about"><h4>About Us</h4>Privacy &amp; security</div>
      <div class="footer__col footer__col--tools"><h4>Tools</h4>Ppsychological safety<br>Harlow culture scan<br>Developer culture scan</div>
    </footer>
  </div>
</section>

<!-- Screen 3: results -->
<section class="stage stage--results">
  <div class="screen">
    <header class="app-header">
      <div class="brand"><div class="brand__name">CREW LIFTERS</div><div class="brand__by">by Velmor Institute</div></div>
      <div class="app-header__bar"></div>
      <a class="nav nav--tools">TOOLS</a><a class="nav nav--about">ABOUT US</a>
      <div class="feedback"><svg width="22" height="22" viewBox="0 0 22 22"><circle cx="11" cy="11" r="9.5" fill="none" stroke="#33b34a" stroke-width="1.6"/><rect x="10" y="9" width="2" height="7" fill="#33b34a"/><circle cx="11" cy="6.5" r="1.2" fill="#33b34a"/></svg>FEEDBACK</div>
    </header>

    <div class="tab tab--active">Jouw Antwoord</div>
    <div class="tab tab--idle">Resultaten</div>
    <div class="tab-rule"></div>
    <div class="toggle-label">Percentages</div>
    <div class="toggle"></div>

    <div class="chart-card" style="top:240px;height:500px">
      <p>Nemo enim ipsam voluptatem quia voluptas sit aspernatur aut odit aut fugit, sed quia consequuntur magni dolores eos qui ratione voluptatem sequi nesciunt.</p>
      <svg width="849" height="500" viewBox="0 0 849 500">
        <line x1="100" y1="133" x2="100" y2="414" stroke="#333" stroke-width="1.5"/>
        <line x1="100" y1="414" x2="771" y2="414" stroke="#333" stroke-width="1.5"/>
        <text x="68" y="202">2</text><text x="68" y="321">1</text>
        <rect x="287" y="297" width="37" height="117" fill="#33b34a"/>
        <rect x="517" y="205" width="37" height="209" fill="#33b34a"/>
        <g text-anchor="middle">
          <text x="174" y="450">zeer oneens</text><text x="305" y="450">oneens</text><text x="422" y="450">neutraal</text><text x="535" y="450">eens</text><text x="658" y="450">zeer eens</text>
        </g>
      </svg>
    </div>

    <div class="chart-card" style="top:773px;height:484px">
      <p style="top:36px">Nemo enim ipsam voluptatem quia voluptas sit aspernatur aut odit aut fugit, sed quia consequuntur magni dolores eos qui ratione voluptatem sequi nesciunt.</p>
      <svg width="849" height="484" viewBox="0 0 849 484">
        <line x1="100" y1="133" x2="100" y2="410" stroke="#333" stroke-width="1.5"/>
        <line x1="100" y1="410" x2="771" y2="410" stroke="#333" stroke-width="1.5"/>
        <text x="68" y="200">2</text><text x="68" y="317">1</text>
        <rect x="156" y="293" width="37" height="117" fill="#33b34a"/>
        <rect x="287" y="201" width="37" height="209" fill="#33b34a"/>
        <g text-anchor="middle">
          <text x="174" y="446">zeer oneens</text><text x="305" y="446">oneens</text><text x="422" y="446">neutraal</text><text x="535" y="446">eens</text><text x="658" y="446">zeer eens</text>
        </g>
      </svg>
    </div>

    <footer class="footer">
      <div class="footer__meta">© 2020 Quillbyte for Velmor Institute<br>Tools that help your teams further.<br><br>Need more help? We are happy to help you.</div>
      <div class="footer__col footer__col--about"><h4>About Us</h4>Privacy &amp; security</div>
      <div class="footer__col footer__col--tools"><h4>Tools</h4>Ppsychological safety<br>Harlow culture scan<br>Developer culture scan</div>
    </footer>
  </div>
</section>

</body>
</html>
```